Brightwell Giving Inc

We need a full re-design of our non-profit organization website (www.brightwellgiving.org). Ideally, we are looking to make it more attractive, user-friendly, and interactive with our business model.

Please make sure to user colors that ago with our logo.

We need a homepage done and we also need a content page done where we will use for the other pages to fill with content.

Target Market(s)

Clothes/textiles donations.

Industry/Entity Type

Charity

Number of Pages Required

2 page

Colors

Designer to choose colors to be used in the design.

Requirements
Must have
• It must match the styling of our logo and same colors as current website. (www.brightwellgiving.org)
Nice to have
• Sleek homepage that is easy to understand and get our main points across.

```html
<!DOCTYPE html>
<html lang="en">
<head>
<meta charset="utf-8">
<title>Brightwell Giving – Home</title>
<link rel="stylesheet" href="https://fonts.googleapis.com/css2?family=Crimson+Text:wght@400;600;700&family=Open+Sans:ital,wght@0,400;0,600;0,700;1,400&display=swap">
<style>
:root{
  --green:#3e7d1c;
  --green-dark:#2d6412;
  --green-light:#5aa82b;
  --yellow:#fcc200;
  --red:#e2141c;
  --paper:#f1f1ef;
  --white:#ffffff;
  --ink:#2b2b2b;
  --muted:#555;
}
*{box-sizing:border-box;margin:0;padding:0}
html,body{width:1200px;height:4433px;overflow:hidden}
body{position:relative;background:var(--paper);font-family:"Open Sans",Arial,sans-serif;color:var(--ink)}
.serif{font-family:"Crimson Text",Georgia,serif}
section,header,footer{position:absolute;left:0;width:1200px}

/* header */
.site-header{top:0;height:142px;z-index:3}
.brand{position:absolute;left:78px;top:30px;display:flex;align-items:center;gap:10px}
.brand-mark{width:34px;height:34px;background:var(--yellow);border-radius:50%}
.brand-name{font-family:"Crimson Text",Georgia,serif;font-weight:700;font-size:22px;color:var(--green-dark);line-height:1}
.brand-tag{position:absolute;left:78px;top:74px;font-size:10px;color:var(--green-dark)}
.toll{position:absolute;right:80px;top:18px;display:flex;align-items:center;gap:12px;font-family:"Crimson Text",Georgia,serif;font-weight:700;font-size:24px;color:var(--white)}
.toll .phone-dot{width:40px;height:40px;border-radius:50%;background:var(--red);display:flex;align-items:center;justify-content:center}
.main-nav{position:absolute;left:285px;top:88px;width:915px;height:45px;background:var(--green);border-radius:40px 0 0 0;display:flex;align-items:center;gap:34px;padding-left:36px;border-bottom:3px solid var(--green-light)}
.main-nav a{color:var(--white);text-decoration:none;font-size:14px;font-weight:600;text-transform:uppercase}

/* hero */
.hero{top:0;height:674px}
.hero-photo{position:absolute;inset:0;background:linear-gradient(100deg,#6e6a63 0%,#a59a8c 35%,#c9b9a0 55%,#7d8790 80%,#5b6470 100%)}
.hero-head{position:absolute;left:200px;top:300px;width:800px;text-align:center;font-family:"Crimson Text",Georgia,serif;font-size:62px;line-height:1.05;color:var(--white);font-weight:600;text-shadow:0 2px 8px rgba(0,0,0,.4)}
.btn{display:inline-block;background:var(--red);color:var(--white);border:4px solid var(--yellow);border-radius:30px;font-family:"Crimson Text",Georgia,serif;font-weight:700;font-size:22px;text-transform:uppercase;padding:6px 28px}
.hero .btn{position:absolute;left:493px;top:458px}

/* welcome */
.welcome{top:674px;height:326px;background:var(--green);text-align:center;color:var(--white)}
.welcome h2{margin-top:66px;font-family:"Crimson Text",Georgia,serif;font-size:44px;font-weight:700;letter-spacing:1px}
.welcome p{width:1010px;margin:18px auto 0;font-size:14px;line-height:1.85}
.pill-btn{position:absolute;left:50%;transform:translateX(-50%);z-index:2}

/* how it works */
.how{top:1000px;height:1181px;overflow:hidden}
.how svg.wave{position:absolute;left:0;top:0}
.how h2{position:absolute;top:88px;width:100%;text-align:center;font-family:"Crimson Text",Georgia,serif;font-size:48px;font-weight:700;color:var(--green)}
.step-photo{position:absolute;width:270px;height:270px;border-radius:50%;border:8px solid var(--green-light)}
.step-text{position:absolute;width:470px}
.step-text h3{font-family:"Crimson Text",Georgia,serif;font-size:30px;line-height:1.1;font-weight:600;color:var(--green)}
.step-text p{margin-top:14px;font-size:14px;line-height:1.6;color:var(--ink)}
.step-right{text-align:right}

/* quote */
.quote{top:2181px;height:287px;background:linear-gradient(90deg,#4e6c25,#6b8a3a 50%,#4e6c25)}
.quote p{position:absolute;top:100px;width:100%;text-align:center;font-size:36px;font-style:italic;color:var(--white);line-height:1.25}
.quote .mark{position:absolute;font-family:"Crimson Text",Georgia,serif;font-size:160px;color:rgba(255,255,255,.35);line-height:1}
.quote .arrow{position:absolute;top:120px}

/* donate */
.donate{top:2468px;height:472px;text-align:center}
.donate h2{margin-top:64px;font-family:"Crimson Text",Georgia,serif;font-size:46px;font-weight:700;color:var(--green)}
.donate .sub{font-size:15px;font-style:italic;color:var(--ink)}
.levels{position:absolute;left:110px;top:156px;display:flex;gap:21px}
.level{width:200px;height:287px;background:var(--white);border-radius:6px;box-shadow:0 2px 6px rgba(0,0,0,.15);position:relative}
.level-tag{position:relative;height:120px;color:var(--white);font-family:"Crimson Text",Georgia,serif;font-weight:700}
.level-tag svg{position:absolute;left:-8px;top:14px}
.level-tag span{position:relative;display:block;padding-top:38px;font-size:18px}
.level-tag b{position:relative;display:block;font-size:24px}
.level .mark-dot{position:absolute;left:80px;top:188px;width:40px;height:40px;border-radius:50%;background:var(--yellow)}

/* mission */
.mission{top:2940px;height:334px}
.mission svg{position:absolute;left:0;top:0}
.mission h2{position:absolute;left:80px;top:90px;font-family:"Crimson Text",Georgia,serif;font-size:40px;font-weight:700;color:var(--white)}
.mission p{position:absolute;left:80px;top:148px;width:680px;font-size:14px;font-style:italic;line-height:1.7;color:var(--white)}
.mission-photo{position:absolute;left:792px;top:-8px;width:376px;height:385px;border-radius:8px;background:linear-gradient(160deg,#6f4a35,#a77c5f 40%,#3f7f3a 75%,#c8a56f)}

/* news */
.news{top:3274px;height:597px;text-align:center}
.news h2{margin-top:70px;font-family:"Crimson Text",Georgia,serif;font-size:48px;font-weight:700;color:var(--green)}
.news-grid{position:absolute;left:80px;top:148px;display:flex;gap:33px;text-align:left}
.news-card{width:326px;height:405px;background:var(--white);box-shadow:0 2px 6px rgba(0,0,0,.12)}
.news-img{height:205px}
.news-meta{display:flex;gap:40px;padding:16px 18px 0;font-size:13px;font-weight:600;color:var(--green)}
.news-meta span{display:flex;align-items:center;gap:6px}
.news-card p{padding:16px 18px;font-family:"Crimson Text",Georgia,serif;font-size:18px;line-height:1.4;color:var(--ink)}

/* banner */
.banner{top:3871px;height:172px;background:var(--yellow)}
.banner h3{position:absolute;left:80px;top:45px;width:680px;font-family:"Crimson Text",Georgia,serif;font-size:34px;line-height:1.2;font-weight:600;color:var(--green-dark)}
.banner .call{position:absolute;left:852px;top:68px;display:flex;align-items:center;gap:12px;background:var(--red);color:var(--white);border-radius:30px;padding:6px 24px 6px 10px;font-family:"Crimson Text",Georgia,serif;font-size:26px;font-weight:700}
.banner .call i{width:36px;height:36px;border-radius:50%;background:var(--white);display:flex;align-items:center;justify-content:center}

/* footer */
.site-footer{top:4043px;height:390px;background:var(--green);color:var(--white)}
.foot-col{position:absolute;top:46px}
.foot-col h4{font-family:"Crimson Text",Georgia,serif;font-size:20px;font-weight:600;text-transform:uppercase;margin-bottom:14px}
.foot-col ul{list-style:none;font-size:14px;line-height:1.9}
.foot-col li::before{content:"";display:inline-block;width:6px;height:6px;border-radius:50%;background:var(--yellow);margin-right:12px;vertical-align:middle}
.contact-item{display:flex;gap:10px;margin-bottom:22px;font-size:14px;line-height:1.5}
.contact-item strong{color:var(--yellow);font-weight:600;display:block}
.foot-brand{position:absolute;left:880px;top:132px;text-align:center;width:240px}
.foot-brand .brand-name{color:var(--white);font-size:24px}
.foot-brand small{display:block;font-size:11px;margin-top:6px}
.social{width:34px;height:34px;border-radius:50%;background:#1b8fe0;margin:14px auto 0}
.copyright{position:absolute;left:0;bottom:0;width:100%;height:44px;background:var(--green-dark);text-align:center;line-height:44px;font-size:13px}
</style>
</head>
<body>

<section class="hero">
  <div class="hero-photo" role="img" aria-label="Two smiling volunteers loading donation boxes of clothing into a car"></div>
  <h1 class="hero-head">Think Globally While Donating Locally</h1>
  <a class="btn">Donate Now</a>
</section>

<header class="site-header">
  <div class="brand"><span class="brand-mark"></span><span class="brand-name">BRIGHTWELL GIVING</span></div>
  <div class="brand-tag">Think Globally while Donating Locally</div>
  <div class="toll">Toll Free :
    <span class="phone-dot"><svg width="20" height="20" viewBox="0 0 24 24"><path fill="#fff" d="M6.6 10.8a15 15 0 0 0 6.6 6.6l2.2-2.2c.3-.3.7-.4 1-.2 1.1.4 2.3.6 3.6.6.6 0 1 .4 1 1V20c0 .6-.4 1-1 1A17 17 0 0 1 3 4c0-.6.4-1 1-1h3.5c.6 0 1 .4 1 1 0 1.3.2 2.5.6 3.6.1.3 0 .7-.2 1z"/></svg></span>
    (855) 555-0142</div>
  <nav class="main-nav">
    <a>Home</a><a>Missions</a><a>Family</a><a>How it works</a><a>About us</a><a>Sponsors</a><a>News</a><a>Donate</a><a>Wall of need</a>
  </nav>
</header>

<section class="welcome">
  <h2>WELCOME TO BRIGHTWELL GIVING</h2>
  <p>Brightwell Giving is a non-profit organization that was created for one purpose: helping the less fortunate in our country's time of greatest need. Started in 2007, Brightwell Giving has been a dedicated member of its local communities over the past four years. The company's clothing collection efforts have allowed it to provide some of the neediest members of the community to clothe themselves and their families. The company's goal is to ensure that some of the most basic needs of the community's members are met thru the philanthropic efforts of the organizations members and contributors.</p>
</section>
<a class="btn pill-btn" style="top:976px">Learn More</a>

<section class="how">
  <svg class="wave" width="1200" height="1181" viewBox="0 0 1200 1181">
    <path d="M0,0 L190,0 C120,140 130,300 260,380 C420,470 720,440 1000,480 C1200,510 1200,540 1200,540 L1200,760 C920,700 560,720 420,790 C250,880 190,1030 330,1181 L0,1181 Z" fill="#fcc200" stroke="#5aa82b" stroke-width="4"/>
  </svg>
  <h2>HOW IT WORKS</h2>

  <div class="step-photo" style="left:160px;top:252px;background:linear-gradient(135deg,#c9a77c,#8c6a48)" role="img" aria-label="Hands holding a cardboard box labelled for clothing donations"></div>
  <div class="step-text" style="left:517px;top:240px">
    <h3>Drop Off Clothing At Your Closest Donation Bin.</h3>
    <p>We have different collection procedures. For outdoors we can place a donation bin, a metal container about 48"L X 48"WX66"H.</p>
  </div>

  <div class="step-text step-right" style="left:210px;top:550px;width:470px">
    <h3>We Pick It Up And Take It To Our Sorting Facility</h3>
    <p>After our drivers pick up the clothing from our designated donation locations, the items are taken to our sorting facility where they are separated.</p>
  </div>
  <div class="step-photo" style="left:762px;top:505px;background:linear-gradient(135deg,#6aa04a,#d9cdb3)" role="img" aria-label="Volunteers in green shirts sorting donated clothes into boxes"></div>

  <div class="step-photo" style="left:155px;top:830px;background:linear-gradient(135deg,#b48a6e,#e6d3bd)" role="img" aria-label="Two children holding a handwritten thank you sign"></div>
  <div class="step-text" style="left:517px;top:900px">
    <h3>Charities Get Clothing. We Pay You For The Clothes.</h3>
    <p>Once we are done distributing our donated clothing to their appropriate channels, the proceeds from the sales are distributed in two ways.</p>
  </div>
</section>

<section class="quote" role="img" aria-label="Soft green backdrop of many hands joined around a heart">
  <span class="mark" style="left:210px;top:40px">&ldquo;</span>
  <span class="mark" style="left:880px;top:150px">&rdquo;</span>
  <svg class="arrow" style="left:72px" width="24" height="50" viewBox="0 0 24 50"><path d="M20 2 L4 25 L20 48" fill="none" stroke="#fff" stroke-width="2"/></svg>
  <svg class="arrow" style="right:72px" width="24" height="50" viewBox="0 0 24 50"><path d="M4 2 L20 25 L4 48" fill="none" stroke="#fff" stroke-width="2"/></svg>
  <p>Our Goal Is To Be With And Within The<br>Community</p>
</section>

<section class="donate">
  <h2>DONATE</h2>
  <div class="sub">Think Globally While Donating Locally</div>
  <div class="levels">
    <div class="level"><div class="level-tag"><svg width="216" height="110" viewBox="0 0 216 110"><path d="M0 0 H216 V70 L108 100 L0 70 Z" fill="#4f9d25"/><path d="M0 70 L8 78 L8 62 Z M216 70 L208 78 L208 62 Z" fill="#2d6412"/></svg><span>LEVEL 1</span><b>$1000</b></div><span class="mark-dot"></span></div>
    <div class="level"><div class="level-tag"><svg width="216" height="110" viewBox="0 0 216 110"><path d="M0 0 H216 V70 L108 100 L0 70 Z" fill="#4f9d25"/></svg><span>LEVEL 2</span><b>$1000-$2500</b></div><span class="mark-dot"></span></div>
    <div class="level"><div class="level-tag"><svg width="216" height="110" viewBox="0 0 216 110"><path d="M0 0 H216 V70 L108 100 L0 70 Z" fill="#4f9d25"/></svg><span>LEVEL 3</span><b>$2500-$5000</b></div><span class="mark-dot"></span></div>
    <div class="level"><div class="level-tag"><svg width="216" height="110" viewBox="0 0 216 110"><path d="M0 0 H216 V70 L108 100 L0 70 Z" fill="#4f9d25"/></svg><span>LEVEL 4</span><b>$5000-$10,000</b></div><span class="mark-dot"></span></div>
    <div class="level"><div class="level-tag"><svg width="216" height="110" viewBox="0 0 216 110"><path d="M0 0 H216 V70 L108 100 L0 70 Z" fill="#4f9d25"/></svg><span>LEVEL 5</span><b>$10,000-$25,000</b></div><span class="mark-dot"></span></div>
  </div>
</section>

<section class="mission">
  <svg width="1200" height="334" viewBox="0 0 1200 334"><path d="M0 0 H1200 V240 C1000 250 880 300 700 310 L0 310 Z" fill="#3e7d1c" stroke="#5aa82b" stroke-width="6"/></svg>
  <h2>MISION</h2>
  <p>Brightwell Giving has a two part mission to help local communities while helping the planet. The average American discards 68 lbs of clothing annually. That is 1,325,340,196 lbs for New York State alone and 21,201,400,000 lbs for the U.S. every year!</p>
  <div class="mission-photo" role="img" aria-label="Smiling young woman holding a cardboard donation box full of clothes"></div>
</section>
<a class="btn pill-btn" style="top:2915px">Learn More</a>

<section class="news">
  <h2>LATEST NEWS</h2>
  <div class="news-grid">
    <article class="news-card">
      <div class="news-img" role="img" aria-label="Printed tri-fold charity flyer on a table" style="background:linear-gradient(135deg,#d8d2c4,#8a7d6a)"></div>
      <div class="news-meta"><span><svg width="14" height="14" viewBox="0 0 14 14"><rect x="1" y="2" width="12" height="11" rx="1" fill="#fcc200"/></svg>May 16, 2017</span><span><svg width="14" height="14" viewBox="0 0 14 14"><circle cx="7" cy="4" r="3" fill="#fcc200"/><path d="M1 14a6 6 0 0 1 12 0z" fill="#fcc200"/></svg>Admin</span></div>
      <p>Brightwell Giving created the Flyer for Inform The People In Manhattan To help others by giving donation.</p>
    </article>
    <article class="news-card">
      <div class="news-img" role="img" aria-label="Volunteers and children gathered outdoors at a charity project" style="background:linear-gradient(135deg,#8fb06a,#c9a27c)"></div>
      <div class="news-meta"><span><svg width="14" height="14" viewBox="0 0 14 14"><rect x="1" y="2" width="12" height="11" rx="1" fill="#fcc200"/></svg>April 28, 2017</span><span><svg width="14" height="14" viewBox="0 0 14 14"><circle cx="7" cy="4" r="3" fill="#fcc200"/><path d="M1 14a6 6 0 0 1 12 0z" fill="#fcc200"/></svg>Admin</span></div>
      <p>We are starting the charity projects to collect funds on FundCircle</p>
    </article>
    <article class="news-card">
      <div class="news-img" role="img" aria-label="Group of volunteers holding donation signs" style="background:linear-gradient(135deg,#e4e1da,#a9b7c4)"></div>
      <div class="news-meta"><span><svg width="14" height="14" viewBox="0 0 14 14"><rect x="1" y="2" width="12" height="11" rx="1" fill="#fcc200"/></svg>May 16, 2017</span><span><svg width="14" height="14" viewBox="0 0 14 14"><circle cx="7" cy="4" r="3" fill="#fcc200"/><path d="M1 14a6 6 0 0 1 12 0z" fill="#fcc200"/></svg>Admin</span></div>
      <p>Brightwell Giving created the Flyer for Inform The People In Manhattan To help others by giving donation.</p>
    </article>
  </div>
</section>

<section class="banner">
  <h3>Brightwell Giving donated to Orphan House in Ukraine</h3>
  <div class="call"><i><svg width="18" height="18" viewBox="0 0 24 24"><path fill="#e2141c" d="M6.6 10.8a15 15 0 0 0 6.6 6.6l2.2-2.2c.3-.3.7-.4 1-.2 1.1.4 2.3.6 3.6.6.6 0 1 .4 1 1V20c0 .6-.4 1-1 1A17 17 0 0 1 3 4c0-.6.4-1 1-1h3.5c.6 0 1 .4 1 1 0 1.3.2 2.5.6 3.6.1.3 0 .7-.2 1z"/></svg></i>(855) 555-0142</div>
</section>

<footer class="site-footer">
  <div class="foot-col" style="left:80px"><h4>Sitemap</h4>
    <ul><li>Home</li><li>Missions</li><li>Family</li><li>How it works</li><li>About Us</li><li>Sponsors</li><li>News</li><li>Donate</li><li>Wall of needs</li></ul></div>
  <div class="foot-col" style="left:345px"><h4>Quick Links</h4>
    <ul><li>Welcome</li><li>Donation Recipients</li><li>Recent News</li><li>Donation in Europe</li></ul></div>
  <div class="foot-col" style="left:590px"><h4>Contact Us</h4>
    <div class="contact-item"><svg width="16" height="22" viewBox="0 0 16 22"><path d="M8 0a8 8 0 0 0-8 8c0 6 8 14 8 14s8-8 8-14a8 8 0 0 0-8-8zm0 11a3 3 0 1 1 0-6 3 3 0 0 1 0 6z" fill="#fcc200"/></svg><div><strong>New York Offices</strong>42 Orchard Ln Hudson NY 12534</div></div>
    <div class="contact-item"><svg width="16" height="22" viewBox="0 0 16 22"><path d="M8 0a8 8 0 0 0-8 8c0 6 8 14 8 14s8-8 8-14a8 8 0 0 0-8-8zm0 11a3 3 0 1 1 0-6 3 3 0 0 1 0 6z" fill="#fcc200"/></svg><div><strong>Thrift Store</strong>87 Meadow Rd Hudson</div></div>
    <div class="contact-item"><svg width="16" height="22" viewBox="0 0 16 22"><path d="M8 0a8 8 0 0 0-8 8c0 6 8 14 8 14s8-8 8-14a8 8 0 0 0-8-8zm0 11a3 3 0 1 1 0-6 3 3 0 0 1 0 6z" fill="#fcc200"/></svg><div><strong>Ny Warehouse</strong>1160 River Rd Catskill NY 12451</div></div>
  </div>
  <div class="foot-brand">
    <span class="brand-name">BRIGHTWELL GIVING</span>
    <small>Think Globally while Donating Locally</small>
    <div class="social"></div>
  </div>
  <div class="copyright">©Brightwell Giving - 2018 All Right Reserved.</div>
</footer>

</body>
</html>
```